creative design for a downloadable PDF

I have a PDF document that needs some creative inspiration on two pages. This PDF will be available for download from our website and contains information on a new service offering. The general design elements are finished and will not be altered: the cover page, headers/footers, color scheme, and back page are all fixed. We just have a 'Table of Contents' page and a 'Workflow' page that are uninteresting and lack inspiration. The Workflow page in particular is concerning as it fails to convey our step-by-step approach to project management and how our customers progress through the steps over time. We had a simple bulleted list (see the MS Word Doc), then went to 'tiles' which zigzag across the page (see the PDF). Anyway we need someone to display this in a more thoughtful and easily understood way.

```html
<!DOCTYPE html>
<html lang="en">
<head>
<meta charset="utf-8">
<title>The Route Workflow</title>
<link rel="stylesheet" href="https://fonts.googleapis.com/css2?family=Fira+Sans:wght@700&family=Roboto:wght@400;500;700;900&display=swap">
<style>
  :root{
    --stage:#e9ecef;
    --band:#1c7cb6;
    --band-dot:#2f8fc6;
    --page:#e3f3fc;
    --ink:#105f8f;
    --bright:#05adea;
    --dark:#0c5f8e;
    --num-bright:#4cc6f2;
    --num-dark:#2e83b3;
    --white:#ffffff;
  }
  *{box-sizing:border-box;margin:0;padding:0}
  html,body{width:1162px;height:1200px;overflow:hidden;background:var(--stage)}
  body{font-family:"Roboto",Arial,sans-serif;position:relative}
  .page{position:absolute;left:181px;top:78px;width:800px;height:1044px;background:var(--page);overflow:hidden}
  .page-header{position:absolute;left:0;top:0;width:100%;height:70px;background:var(--band)}
  .page-header .doc-title{position:absolute;left:72px;top:30px;color:var(--white);font-weight:500;font-size:12px}
  .page-header .page-no{position:absolute;left:729px;top:30px;color:var(--white);font-weight:500;font-size:12px}
  .page-title{position:absolute;left:0;top:104px;width:100%;text-align:center;font-family:"Fira Sans",Arial,sans-serif;font-weight:700;font-size:39px;color:var(--ink)}
  .title-rule{position:absolute;left:318px;top:154px}
  .tile{position:absolute;width:152px;height:106px;color:var(--white)}
  .tile.bright{background:var(--bright)}
  .tile.dark{background:var(--dark)}
  .tile .num{position:absolute;right:8px;top:2px;font-weight:900;font-size:26px;letter-spacing:.5px}
  .tile.bright .num{color:var(--num-bright)}
  .tile.dark .num{color:var(--num-dark)}
  .tile .icon{position:absolute;left:7px;top:8px;width:24px;height:24px}
  .tile .text{position:absolute;left:6px;right:6px;top:47px;font-size:9.3px;line-height:11px}
  .link{position:absolute}
  .link.bright{background:var(--bright)}
  .link.dark{background:var(--dark)}
  .tagline{position:absolute;left:0;top:934px;width:100%;text-align:center;font-weight:700;font-size:21px;color:var(--ink);word-spacing:1px}
  .page-footer{position:absolute;left:0;bottom:0;width:100%;height:45px;background:var(--band);color:var(--white);font-weight:500;font-size:13px;text-align:center;line-height:45px}
</style>
</head>
<body>
<svg width="0" height="0" style="position:absolute">
  <symbol id="step-icon" viewBox="0 0 24 24">
    <rect x="2.5" y="3.5" width="19" height="17" rx="2" fill="none" stroke="#fff" stroke-width="1.4"/>
    <line x1="2.5" y1="8" x2="21.5" y2="8" stroke="#fff" stroke-width="1.4"/>
    <line x1="6" y1="12" x2="18" y2="12" stroke="#fff" stroke-width="1.2"/>
    <line x1="6" y1="15.5" x2="14" y2="15.5" stroke="#fff" stroke-width="1.2"/>
  </symbol>
</svg>

<main class="page">
  <header class="page-header">
    <span class="doc-title">The ROUTE Purchasing Experience</span>
    <span class="page-no">3</span>
  </header>

  <h1 class="page-title">The Route Workflow</h1>
  <svg class="title-rule" width="172" height="14" viewBox="0 0 172 14">
    <line x1="1" y1="7" x2="171" y2="7" stroke="#105f8f" stroke-width="2"/>
    <line x1="1" y1="1" x2="1" y2="13" stroke="#105f8f" stroke-width="2"/>
    <line x1="171" y1="1" x2="171" y2="13" stroke="#105f8f" stroke-width="2"/>
  </svg>

  <!-- connectors between rows -->
  <div class="link dark" style="left:719px;top:330px;width:64px;height:40px;border-radius:0 0 0 0"></div>
  <div class="link dark" style="left:25px;top:466px;width:62px;height:18px"></div>
  <div class="link bright" style="left:25px;top:484px;width:62px;height:20px"></div>
  <div class="link bright" style="left:719px;top:602px;width:64px;height:16px"></div>
  <div class="link dark" style="left:719px;top:618px;width:64px;height:22px"></div>
  <div class="link dark" style="left:25px;top:738px;width:62px;height:18px"></div>
  <div class="link bright" style="left:25px;top:756px;width:62px;height:20px"></div>

  <!-- row 1 -->
  <div class="tile bright" style="left:25px;top:227px;border-radius:8px 0 0 8px"><svg class="icon" style="display:none"></svg><span class="num">01</span><p class="text">Medical Device Original Equipment Manufacturer (OEM) creates account on the Heron Medical (HMPS) web portal.</p></div>
  <div class="tile dark" style="left:177px;top:227px"><span class="num">02</span><p class="text">OEM digitally signs ‘readiness checklist’ to gain access to downloadables</p></div>
  <div class="tile bright" style="left:329px;top:227px"><svg class="icon"><use href="#step-icon"/></svg><span class="num">03</span><p class="text">The readiness checklist protects the OEM’s investment by confirming critical benchmarks, AND</p></div>
  <div class="tile dark" style="left:480px;top:227px"><svg class="icon"><use href="#step-icon"/></svg><span class="num">04</span><p class="text">Necessary data and deliverables to HMPS are immediately available</p></div>
  <div class="tile bright" style="left:632px;top:227px;width:151px;border-radius:0 8px 0 0"><svg class="icon"><use href="#step-icon"/></svg><span class="num">05</span><p class="text">OEM downloads eBook #3, Mutual NDA, and ROUTE contract</p></div>

  <!-- row 2 -->
  <div class="tile dark" style="left:25px;top:364px;border-radius:8px 0 0 0"><svg class="icon"><use href="#step-icon"/></svg><span class="num">10</span><p class="text">OEM submits $5K nonrefundable deposit, which is fully creditable to ROUTE or custom development project</p></div>
  <div class="tile bright" style="left:177px;top:364px"><svg class="icon"><use href="#step-icon"/></svg><span class="num">09</span><p class="text">HMPS sends quote for ROUTE routine production to 10K units/yr. pricing, along with credit terms</p></div>
  <div class="tile dark" style="left:329px;top:364px"><svg class="icon"><use href="#step-icon"/></svg><span class="num">08</span><p class="text">HMPS evaluates drawing and verifies that ROUTE is a viable solution for the specific medical device configuration</p></div>
  <div class="tile bright" style="left:480px;top:364px"><svg class="icon"><use href="#step-icon"/></svg><span class="num">07</span><p class="text">OEM uploads critical info such as their top-level assembly drawing (released data only) for evaluation</p></div>
  <div class="tile dark" style="left:632px;top:364px;width:151px;border-radius:0 0 8px 0"><svg class="icon"><use href="#step-icon"/></svg><span class="num">06</span><p class="text">HMPS/OEM sign mutual NDA</p></div>

  <!-- row 3 -->
  <div class="tile bright" style="left:25px;top:500px;border-radius:0 0 0 8px"><svg class="icon"><use href="#step-icon"/></svg><span class="num">11</span><p class="text">OEM downloads DocVault; allowing 24-hour access to restricted doc set to verify contents</p></div>
  <div class="tile dark" style="left:177px;top:500px"><svg class="icon"><use href="#step-icon"/></svg><span class="num">12</span><p class="text">OEM provided with FDA Master File number; allowed time to verify MF on devicereg.org</p></div>
  <div class="tile bright" style="left:329px;top:500px"><svg class="icon"><use href="#step-icon"/></svg><span class="num">13</span><p class="text">OEM and HMPS formalize and sign the ROUTE contract</p></div>
  <div class="tile dark" style="left:480px;top:500px"><svg class="icon"><use href="#step-icon"/></svg><span class="num">14</span><p class="text">OEM and HMPS sign the IP Escrow contract</p></div>
  <div class="tile bright" style="left:632px;top:500px;width:151px;border-radius:0 8px 0 0"><svg class="icon"><use href="#step-icon"/></svg><span class="num">15</span><p class="text">HMPS uploads document set to the Escrow portal with specified security controls</p></div>

  <!-- row 4 -->
  <div class="tile dark" style="left:25px;top:636px;border-radius:0"><svg class="icon"><use href="#step-icon"/></svg><span class="num">16</span><p class="text">Escrow agent releases funds and IP to respective parties</p></div>
  <div class="tile bright" style="left:177px;top:636px"><svg class="icon"><use href="#step-icon"/></svg><span class="num">17</span><p class="text">OEM and HMPS mutually green-light the transaction via secure conference call with escrow agent</p></div>
  <div class="tile dark" style="left:329px;top:636px"><svg class="icon"><use href="#step-icon"/></svg><span class="num">18</span><p class="text">OEM given short term, unrestricted access to the document set to verify contents and accessibility</p></div>
  <div class="tile bright" style="left:480px;top:636px"><svg class="icon"><use href="#step-icon"/></svg><span class="num">19</span><p class="text">Escrow agent verifies receipt of both IP and funds</p></div>
  <div class="tile dark" style="left:632px;top:636px;width:151px;border-radius:0 0 8px 0"><svg class="icon"><use href="#step-icon"/></svg><span class="num">20</span><p class="text">OEM transfers payment balance to Escrow</p></div>

  <!-- row 5 -->
  <div class="tile bright" style="left:25px;top:773px;border-radius:0 8px 8px 8px"><svg class="icon"><use href="#step-icon"/></svg><span class="num">21</span><p class="text">Onus on OEM to complete engineering rationale for adoption with support from HMPS</p></div>

  <p class="tagline">IF YOU ARE READY,&nbsp; THIS TAKES AS LITTLE AS THREE WEEKS</p>

  <footer class="page-footer">www.heronmedsys.com &nbsp;• info@heronmedsys.com &nbsp;•&nbsp; 555-014-2290</footer>
</main>
</body>
</html>
```